Realty Group Needs Classy, Contemporary Letterhead Design

We need a letterhead design for a new realty company located in NY, USA. We buy investment properties to rehabilitate and or keep in our rental portfolio.

```html
<!DOCTYPE html>
<html lang="en">
<head>
<meta charset="utf-8">
<title>Meridian Property Partners — Letterhead</title>
<link href="https://fonts.googleapis.com/css2?family=Open+Sans:wght@400;600;700&display=swap" rel="stylesheet">
<style>
  :root {
    --backdrop: #e9e9e9;
    --paper: #ffffff;
    --brand-purple: #4a2a8c;
    --brand-purple-deep: #35186e;
    --swoosh-grey: #c9c9cc;
    --swoosh-grey-light: #ececee;
    --ink-grey: #6b6b70;
  }
  * { margin: 0; padding: 0; box-sizing: border-box; }
  html, body {
    width: 1200px;
    height: 795px;
    overflow: hidden;
    background: var(--backdrop);
  }
  .letterhead {
    position: absolute;
    left: 340px;
    top: 30px;
    width: 520px;
    height: 736px;
    background: var(--paper);
    box-shadow: 0 6px 24px rgba(0,0,0,0.12);
    overflow: hidden;
  }
  .brand {
    position: absolute;
    left: 38px;
    top: 152px;
    display: flex;
    align-items: center;
    gap: 8px;
  }
  .brand-mark {
    width: 14px;
    height: 14px;
    background: var(--brand-purple);
  }
  .brand-name {
    font-family: "Open Sans", sans-serif;
    font-weight: 600;
    font-size: 19px;
    color: var(--brand-purple);
    line-height: 1;
  }
  .contact {
    position: absolute;
    right: 30px;
    top: 34px;
    list-style: none;
    font-family: "Open Sans", sans-serif;
    font-size: 7.5px;
    color: var(--ink-grey);
    text-align: right;
    line-height: 12px;
  }
  .contact li {
    display: flex;
    justify-content: flex-end;
    align-items: center;
    gap: 5px;
  }
  .contact-icon {
    width: 8px;
    height: 8px;
    background: var(--brand-purple);
    display: inline-flex;
    align-items: center;
    justify-content: center;
  }
  .contact-icon svg { width: 6px; height: 6px; fill: #fff; }
  .footer-wave {
    position: absolute;
    left: 0;
    bottom: 0;
    width: 520px;
    height: 190px;
  }
  .website {
    position: absolute;
    left: 30px;
    bottom: 74px;
    font-family: "Open Sans", sans-serif;
    font-weight: 700;
    font-size: 10px;
    color: var(--brand-purple);
  }
</style>
</head>
<body>
  <main class="letterhead">
    <ul class="contact">
      <li>(000) 0123 456 780 <span class="contact-icon"><svg viewBox="0 0 10 10"><path d="M2 1h2l1 2-1.2 1a5 5 0 0 0 2.2 2.2L7 5l2 1v2a1 1 0 0 1-1 1A7 7 0 0 1 1 2a1 1 0 0 1 1-1z"/></svg></span></li>
      <li>(000) 0123 456 781 <span class="contact-icon"><svg viewBox="0 0 10 10"><rect x="1" y="2" width="8" height="6"/></svg></span></li>
      <li>info@meridianpartners.com <span class="contact-icon"><svg viewBox="0 0 10 10"><path d="M1 2h8v6H1z"/></svg></span></li>
      <li>48 Harbor Lane, Albany, NY 12207 <span class="contact-icon"><svg viewBox="0 0 10 10"><path d="M5 0a3.5 3.5 0 0 1 3.5 3.5C8.5 6 5 10 5 10S1.5 6 1.5 3.5A3.5 3.5 0 0 1 5 0z"/></svg></span></li>
    </ul>

    <header class="brand">
      <span class="brand-mark" aria-hidden="true"></span>
      <span class="brand-name">Meridian Property Partners</span>
    </header>

    <div class="website">www.meridianpartners.com</div>

    <svg class="footer-wave" viewBox="0 0 520 190" preserveAspectRatio="none" aria-hidden="true">
      <defs>
        <linearGradient id="swooshGrey" x1="0" y1="0" x2="1" y2="1">
          <stop offset="0" stop-color="#ececee"/>
          <stop offset="0.6" stop-color="#c9c9cc"/>
          <stop offset="1" stop-color="#ececee"/>
        </linearGradient>
        <linearGradient id="swooshPurple" x1="1" y1="0" x2="0" y2="1">
          <stop offset="0" stop-color="#35186e"/>
          <stop offset="0.5" stop-color="#4a2a8c"/>
          <stop offset="1" stop-color="#35186e"/>
        </linearGradient>
      </defs>
      <path d="M520 0 C470 8 440 55 400 105 C355 158 210 160 0 158 L0 190 L520 190 Z" fill="url(#swooshGrey)"/>
      <path d="M520 22 C482 32 452 82 415 125 C372 168 220 172 0 170 L0 190 L520 190 Z" fill="url(#swooshPurple)"/>
    </svg>
  </main>
</body>
</html>
```